Commercial brochure presenting independent commercial activity

I would like to create a commercial brochure for my new professional activity.

This is a personal and not business oriented brochure because I will become an independent project assistant to assist engineering offices with one-off missions.

I want a 4 page A4 brochure

• Page 1: Logo, personal photo
• Page 2 and 3: Personal presentation and presentation of my activities
• Page4: contact information

My target audience: engineering offices and design offices

The objective of the brochure: it is to make my profile interesting so that design offices will want to use my services when there is demand

Sector of activity: food, chemical, pharmaceutical industry
The text of the brochure must remain in French and contain what is in the attached file

On page 1, you must keep a space for a photo of my profile which I will insert later because I do not have it yet and insert my monogram (it can be reworked to be inserted in the brochure)
The image with the logo (K/M) is the color range I want

engineering offices and design offices

industrie alimentaire, chimique, pharmaceutique

Sans Serif

0094D4
00A9DD
6FCCEA
C7EBF8
E9F6FB

• The plate must comply with current codes. Each reader must think that I am dynamic and that my services are of quality and equivalent to the presentation

```html
<!DOCTYPE html>
<html lang="fr">
<head>
<meta charset="utf-8">
<title>Kevin Marchand – Brochure</title>
<link href="https://fonts.googleapis.com/css2?family=Lora:wght@400;500;600;700&family=Poppins:wght@400;500&display=swap" rel="stylesheet">
<style>
  :root{
    --blue-deep:#0094D4;
    --blue:#00A9DD;
    --blue-light:#6FCCEA;
    --blue-pale:#C7EBF8;
    --blue-mist:#E9F6FB;
    --ink:#333;
    --ink-soft:#444;
    --backdrop:#5e5e5e;
    --serif:'Lora', Georgia, serif;
    --sans:'Poppins', Arial, sans-serif;
  }
  *{margin:0;padding:0;box-sizing:border-box}
  html,body{width:907px;height:1200px;overflow:hidden}
  body{background:var(--backdrop);position:relative;font-family:var(--serif);color:var(--ink)}
  .page{position:absolute;width:372px;height:526px;overflow:hidden;background:#fff}
  .page > svg.page-bg{position:absolute;inset:0;width:100%;height:100%}
  .page-cover{left:60px;top:41px}
  .page-expertise{left:474px;top:41px}
  .page-advantage{left:60px;top:597px}
  .page-contact{left:474px;top:597px}

  /* cover */
  .brand{position:absolute;left:0;width:204px;top:66px;text-align:center}
  .brand-mark{display:inline-flex;align-items:center;gap:6px;font-family:var(--serif);font-weight:400;color:var(--blue-deep);font-size:15px;letter-spacing:.3px}
  .brand-dot{width:9px;height:9px;border:1.5px solid var(--blue-deep);border-radius:50%}
  .brand-tagline{font-size:7px;color:var(--blue-deep);margin-top:6px}
  .cover-name{position:absolute;left:36px;top:326px;font-family:var(--serif);font-weight:700;color:var(--blue);font-size:34px;line-height:35px}
  .cover-pitch{position:absolute;left:36px;top:404px;font-size:16px;line-height:19px;color:var(--ink-soft)}
  .contact-block{font-size:11px;line-height:15px;color:#fff}
  .cover-contact{position:absolute;left:36px;top:463px}
  .contact-line{display:flex;align-items:center;gap:4px;white-space:nowrap}
  .contact-line svg{width:9px;height:9px;flex:none}
  .contact-gap{margin-left:10px}

  /* expertise */
  .intro{position:absolute;left:38px;top:17px;width:310px;font-family:var(--sans);font-weight:500;font-size:9.1px;line-height:10.5px;color:#fff}
  .section-title{position:absolute;font-family:var(--serif);font-weight:600;color:var(--blue-deep);font-size:16px}
  .page-expertise .section-title{left:40px;top:115px}
  .page-advantage .section-title{left:35px;top:77px}
  .card{position:absolute;background:var(--blue-mist);border-radius:8px;height:65px}
  .page-expertise .card{left:33px;width:310px}
  .page-advantage .card{left:30px;width:319px}
  .card-icon{position:absolute;left:14px;top:12px;width:40px;height:40px;border-radius:50%;background:var(--blue-deep);display:flex;align-items:center;justify-content:center}
  .card-icon span{width:22px;height:22px;border:1.5px solid #fff;border-radius:50%}
  .card-body{position:absolute;left:61px;top:9px;right:10px}
  .card-title{font-family:var(--serif);font-weight:500;color:var(--blue-deep);font-size:10.2px;line-height:11px;margin-bottom:3px}
  .card-text{font-size:7.1px;line-height:9px;color:var(--ink)}
  .ticks{list-style:none;font-size:7.3px;line-height:9px}
  .ticks li{position:relative;padding-left:9px}
  .ticks li::before{content:"";position:absolute;left:0;top:2px;width:5.5px;height:5.5px;border-radius:50%;background:var(--blue)}
  .ticks-cols{display:flex;gap:12px}

  /* contact page */
  .seal{position:absolute;left:131px;top:253px;width:130px;height:130px;display:flex;flex-direction:column;align-items:center;justify-content:center;text-align:center}
  .seal .brand-mark{font-size:10px;gap:4px}
  .seal .brand-dot{width:6px;height:6px;border-width:1px}
  .seal .brand-tagline{font-size:4.5px;margin-top:3px}
  .closing{position:absolute;left:50px;right:50px;top:409px;text-align:center;font-weight:600;font-size:11.4px;line-height:14.2px;color:var(--ink)}
  .closing-contact{position:absolute;left:0;right:0;top:463px;color:var(--ink);display:flex;flex-direction:column;align-items:center;line-height:16px}
</style>
</head>
<body>

<section class="page page-cover">
  <svg class="page-bg" viewBox="0 0 372 526">
    <defs>
      <linearGradient id="coverSky" x1="0" y1="0" x2="0" y2="1">
        <stop offset="0" stop-color="#fff"/><stop offset="1" stop-color="#E9F6FB"/>
      </linearGradient>
      <linearGradient id="coverWave" x1="0" y1="0" x2="1" y2="1">
        <stop offset="0" stop-color="#00A9DD"/><stop offset="1" stop-color="#0094D4"/>
      </linearGradient>
    </defs>
    <rect width="372" height="526" fill="url(#coverSky)"/>
    <path d="M168 0 C192 62 255 114 372 119 L372 0 Z" fill="url(#coverWave)" role="img" aria-label="Motif de lignes ondulées"/>
    <path d="M0 272 C45 245 105 226 165 222 C260 216 330 262 372 330 L372 526 L0 526 Z" fill="#fff"/>
    <path d="M18 262 C60 240 105 228 150 225" stroke="#0094D4" stroke-width="3" fill="none"/>
    <path d="M298 300 C340 350 352 440 326 526" stroke="#0094D4" stroke-width="6" fill="none"/>
    <circle cx="226" cy="247" r="91" fill="#fff" stroke="#00A9DD" stroke-width="11" role="img" aria-label="Emplacement pour la photo de profil"/>
    <circle cx="311" cy="152" r="25" fill="none" stroke="#00A9DD" stroke-width="1.5"/>
    <circle cx="114" cy="203" r="13" fill="none" stroke="#00A9DD" stroke-width="1.5"/>
    <polygon points="0,455 337,455 329,501 0,501" fill="#00A9DD"/>
  </svg>
  <div class="brand">
    <div class="brand-mark"><span class="brand-dot"></span>Kevin Marchand</div>
    <div class="brand-tagline">Assistant de projet indépendant</div>
  </div>
  <h1 class="cover-name">Kevin<br>Marchand</h1>
  <p class="cover-pitch">Un atout précieux pour votre<br>bureau d'études</p>
  <div class="cover-contact contact-block">
    <div class="contact-line"><svg viewBox="0 0 10 10"><path d="M10 0 L0 4 L4.5 5.5 L6 10 Z" fill="#fff"/></svg>Ch. des Vergers 12 1860 Valdor</div>
    <div class="contact-line"><svg viewBox="0 0 10 10"><rect x=".5" y="1.5" width="9" height="7" fill="none" stroke="#fff"/><path d="M.5 1.5 L5 5.5 L9.5 1.5" fill="none" stroke="#fff"/></svg>kevin@marchand-assist.ch
      <span class="contact-gap"></span><svg viewBox="0 0 10 10"><path d="M2 .8 L3.8 3 L2.8 4 C3.5 5.6 4.5 6.7 6 7.3 L7 6.2 L9.2 8 L8 9.4 C4 9 1 6 .6 2 Z" fill="none" stroke="#fff" stroke-width=".8"/></svg>+41 79 000 12 34</div>
  </div>
</section>

<section class="page page-expertise">
  <svg class="page-bg" viewBox="0 0 372 526">
    <defs>
      <linearGradient id="bannerFill" x1="0" y1="0" x2="1" y2="0">
        <stop offset="0" stop-color="#00A9DD"/><stop offset="1" stop-color="#0094D4"/>
      </linearGradient>
    </defs>
    <path d="M0 0 H372 V70 C300 95 200 104 120 100 C70 96 30 88 0 78 Z" fill="url(#bannerFill)" role="img" aria-label="Bandeau bleu à motif de lignes ondulées"/>
    <path d="M45 90 C150 112 280 110 372 72" stroke="#00A9DD" stroke-width="3" fill="none"/>
    <path d="M90 526 C160 494 260 484 372 484 L372 526 Z" fill="#00A9DD" role="img" aria-label="Vague décorative bleue"/>
    <path d="M300 472 L372 474" stroke="#00A9DD" stroke-width="3"/>
    <path d="M300 480 C330 478 352 478 372 481" stroke="#6FCCEA" stroke-width="2" fill="none"/>
  </svg>
  <p class="intro">Avec plus de 30 ans d'expérience dans l'industrie, je suis un expert chevronné en conception, gestion de projets et sécurité. J'offre mes services d'assistant de projet indépendant pour vous aider à gérer les pics de charge et les besoins spécifiques de votre bureau d'études.Mon expertise</p>
  <h2 class="section-title">Mon expertise</h2>

  <div class="card" style="top:142px">
    <div class="card-icon"><span></span></div>
    <div class="card-body">
      <h3 class="card-title">Conception &amp; Design</h3>
      <ul class="ticks">
        <li>Maquettes 3D (Logiciel CAO 3D)</li>
        <li>Plans, schémas, RI/P&amp;ID, Flowsheets</li>
        <li>Spécifications, catalogues, définition des fournitures</li>
      </ul>
    </div>
  </div>
  <div class="card" style="top:214px">
    <div class="card-icon"><span></span></div>
    <div class="card-body">
      <h3 class="card-title">Gestion de Projets</h3>
      <div class="ticks-cols">
        <ul class="ticks">
          <li>Rédaction d'appels d'offre</li>
          <li>Préparation de budgets</li>
          <li>Réalisation de plannings</li>
        </ul>
        <ul class="ticks">
          <li>Estimations budgétaires</li>
          <li>Réponse aux appels d'offre</li>
        </ul>
      </div>
    </div>
  </div>
  <div class="card" style="top:286px">
    <div class="card-icon"><span></span></div>
    <div class="card-body">
      <h3 class="card-title">Sécurité</h3>
      <ul class="ticks">
        <li>Sécurité machine</li>
        <li>Plans de montage</li>
        <li>Edition de PHS</li>
      </ul>
    </div>
  </div>
  <div class="card" style="top:358px">
    <div class="card-icon"><span></span></div>
    <div class="card-body">
      <h3 class="card-title">Documentation Technique</h3>
      <ul class="ticks">
        <li>DESP</li>
        <li>Documentations spécifiques</li>
      </ul>
    </div>
  </div>
  <div class="card" style="top:430px">
    <div class="card-icon"><span></span></div>
    <div class="card-body">
      <h3 class="card-title">Expertise</h3>
      <p class="card-text">Ma connaissance approfondie de la métallurgie (tuyauterie,<br>serrurerie, chaudronnerie, charpente métallique, montage) me permet<br>de garantir des études complètes et d'éviter les oublis.</p>
    </div>
  </div>
</section>

<section class="page page-advantage">
  <svg class="page-bg" viewBox="0 0 372 528">
    <defs>
      <linearGradient id="photoTone" x1="0" y1="0" x2="1" y2="1">
        <stop offset="0" stop-color="#e6e6e6"/><stop offset=".6" stop-color="#b5b5b5"/><stop offset="1" stop-color="#555"/>
      </linearGradient>
      <linearGradient id="footWave" x1="0" y1="0" x2="1" y2="0">
        <stop offset="0" stop-color="#00A9DD"/><stop offset="1" stop-color="#6FCCEA"/>
      </linearGradient>
    </defs>
    <path d="M95 0 H372 V50 C320 70 262 78 205 74 C155 70 118 45 95 0 Z" fill="url(#photoTone)" role="img" aria-label="Photo : mains sur une tablette affichant le mot succès"/>
    <path d="M95 0 C118 52 162 80 232 80 C292 80 340 66 372 50" stroke="#0094D4" stroke-width="5" fill="none"/>
    <path d="M95 528 C180 488 300 478 372 480 L372 528 Z" fill="url(#footWave)" role="img" aria-label="Vague décorative à motif de lignes"/>
    <path d="M190 490 C260 474 320 470 372 470" stroke="#0094D4" stroke-width="3" fill="none"/>
  </svg>
  <h2 class="section-title">Votre avantage</h2>

  <div class="card" style="top:106px">
    <div class="card-icon"><span></span></div>
    <div class="card-body">
      <h3 class="card-title">Connaissance des besoins des concepteurs<br>et des fabricants</h3>
      <p class="card-text">J'ai travaillé des deux côtés, ce qui me permet de comprendre les défis<br>et les attentes de chacun.</p>
    </div>
  </div>
  <div class="card" style="top:178px">
    <div class="card-icon"><span></span></div>
    <div class="card-body" style="top:12px">
      <h3 class="card-title">Flexibilité</h3>
      <p class="card-text">Je suis disponible pour des missions ponctuelles et à durée déterminée,<br>sans engagement à long terme.</p>
    </div>
  </div>
  <div class="card" style="top:251px">
    <div class="card-icon"><span></span></div>
    <div class="card-body" style="top:12px">
      <h3 class="card-title">Efficacité</h3>
      <p class="card-text">Je peux vous aider à gérer les surcharges de travail et à respecter<br>vos délais</p>
    </div>
  </div>
  <div class="card" style="top:323px">
    <div class="card-icon"><span></span></div>
    <div class="card-body" style="top:12px">
      <h3 class="card-title">Collaboration fluide</h3>
      <p class="card-text">Je suis à votre disposition pour discuter de vos besoins et vous<br>proposer des solutions sur mesure.</p>
    </div>
  </div>
  <div class="card" style="top:395px">
    <div class="card-icon"><span></span></div>
    <div class="card-body" style="top:6px;right:6px">
      <h3 class="card-title">Un atout unique</h3>
      <p class="card-text" style="white-space:nowrap">Malgré mon handicap en fauteuil roulant, je suis totalement opérationnel<br>et mon expérience me permet de vous offrir une expertise de haut niveau.<br>Je suis disponible à 35% dès septembre 2024 et je suis prêt à mettre mon<br>expertise et mon dynamisme au service de votre succès</p>
    </div>
  </div>
</section>

<section class="page page-contact">
  <svg class="page-bg" viewBox="0 0 372 526">
    <defs>
      <linearGradient id="contactSky" x1="0" y1="0" x2="1" y2="1">
        <stop offset="0" stop-color="#00A9DD"/><stop offset="1" stop-color="#6FCCEA"/>
      </linearGradient>
      <radialGradient id="contactWave" cx=".5" cy=".5" r=".5">
        <stop offset="0" stop-color="#C7EBF8" stop-opacity=".55"/><stop offset="1" stop-color="#C7EBF8" stop-opacity="0"/>
      </radialGradient>
    </defs>
    <rect width="372" height="526" fill="url(#contactSky)"/>
    <ellipse cx="200" cy="170" rx="190" ry="120" fill="url(#contactWave)" role="img" aria-label="Motif de lignes ondulées"/>
    <path d="M250 328 C305 326 350 365 372 410 L372 345 C342 316 300 308 260 314 Z" fill="#0094D4"/>
    <path d="M0 440 C40 380 120 330 196 325 C280 322 340 360 372 410 L372 526 L0 526 Z" fill="#fff"/>
    <circle cx="63" cy="5" r="35" fill="none" stroke="#fff" stroke-width="1.5"/>
    <circle cx="268" cy="165" r="23" fill="none" stroke="#fff" stroke-width="1.5"/>
    <circle cx="97" cy="244" r="6" fill="none" stroke="#fff" stroke-width="1.5"/>
    <circle cx="232" cy="276" r="17" fill="none" stroke="#fff" stroke-width="1.5"/>
    <circle cx="41" cy="384" r="22" fill="none" stroke="#fff" stroke-width="1.5"/>
    <circle cx="196" cy="318" r="63" fill="#fff" stroke="#00A9DD" stroke-width="8"/>
  </svg>
  <div class="seal">
    <div class="brand-mark"><span class="brand-dot"></span>Kevin Marchand</div>
    <div class="brand-tagline">Assistant de projet indépendant</div>
  </div>
  <p class="closing">N'hésitez pas à me contacter pour discuter de vos besoins et découvrir comment je peux vous aider à atteindre vos objectifs</p>
  <div class="closing-contact contact-block">
    <div class="contact-line"><svg viewBox="0 0 10 10"><path d="M10 0 L0 4 L4.5 5.5 L6 10 Z" fill="#0094D4"/></svg>Ch. des Vergers 12 1860 Valdor</div>
    <div class="contact-line"><svg viewBox="0 0 10 10"><rect x=".5" y="1.5" width="9" height="7" fill="none" stroke="#0094D4"/><path d="M.5 1.5 L5 5.5 L9.5 1.5" fill="none" stroke="#0094D4"/></svg>kevin@marchand-assist.ch
      <span class="contact-gap"></span><svg viewBox="0 0 10 10"><path d="M2 .8 L3.8 3 L2.8 4 C3.5 5.6 4.5 6.7 6 7.3 L7 6.2 L9.2 8 L8 9.4 C4 9 1 6 .6 2 Z" fill="none" stroke="#0094D4" stroke-width=".8"/></svg>+41 79 000 12 34</div>
  </div>
</section>

</body>
</html>
```